Stationary for a Consulting Firm
The Summit Compass Incorporated
Project: Stationary for a Consulting Firm
Stationary for a Consulting Firm - Consulting
Creative Brief
Professional
Dr. Gordon T. Feld
President
47 Maple Crest Okotoks, AB T2Q 4M9
gfeld@summitcompass.ca
www.summitcompass.ca
Business Cards, Stationary, Fax Cover Sheet, and Envelopes are required
Canada's Summit Compass

```html
<!DOCTYPE html>
<html lang="en">
<head>
<meta charset="utf-8">
<title>The Summit Compass Incorporated – Business Card</title>
<link href="https://fonts.googleapis.com/css2?family=Open+Sans:wght@400;600;700&display=swap" rel="stylesheet">
<style>
  :root {
    --bg: #e9edf1;
    --card-white: #ffffff;
    --brand-blue: #1d7fb8;
    --brand-deep: #0f5f93;
    --brand-teal: #3aa6cf;
    --brand-light: #a9d9ee;
    --text-grey: #5d6770;
    --rule: #9fcde4;
  }
  * { box-sizing: border-box; margin: 0; padding: 0; }
  html, body { width: 1200px; height: 874px; overflow: hidden; }
  body {
    background: var(--bg);
    font-family: "Open Sans", Arial, sans-serif;
    position: relative;
  }
  .card {
    position: absolute;
    top: 277px;
    width: 560px;
    height: 320px;
    border-radius: 18px;
    overflow: hidden;
    box-shadow: 0 6px 18px rgba(20, 50, 80, 0.18);
  }
  .card-front { left: 30px; background: var(--card-white); }
  .card-back {
    left: 610px;
    background: linear-gradient(160deg, var(--brand-teal) 0%, var(--brand-blue) 55%, var(--brand-deep) 100%);
  }

  /* front */
  .brand {
    position: absolute;
    left: 38px;
    top: 62px;
    width: 180px;
    text-align: center;
  }
  .brand-dot {
    width: 54px; height: 54px;
    border-radius: 50%;
    background: var(--brand-blue);
    margin: 0 auto 12px;
  }
  .brand-name {
    color: var(--brand-blue);
    font-weight: 700;
    font-size: 24px;
    line-height: 1.05;
    letter-spacing: 1px;
  }
  .divider {
    position: absolute;
    left: 238px; top: 40px;
    width: 1px; height: 160px;
    background: var(--rule);
  }
  .contact {
    position: absolute;
    left: 256px; top: 40px;
    color: var(--text-grey);
    font-size: 10.5px;
    line-height: 1.5;
  }
  .contact-name { color: var(--brand-blue); font-weight: 600; font-size: 15px; line-height: 1.3; }
  .contact-title { font-size: 10px; margin-bottom: 12px; }
  .contact-address { margin-bottom: 8px; }
  .contact-line { display: flex; align-items: center; gap: 6px; }
  .contact-line svg { width: 10px; height: 10px; flex: none; }
  .contact-web { color: var(--brand-deep); font-weight: 700; }
  .footer-band {
    position: absolute;
    left: 0; right: 0; bottom: 0;
    height: 84px;
    background: linear-gradient(180deg, var(--brand-light) 0%, var(--brand-teal) 40%, var(--brand-blue) 70%, var(--brand-deep) 100%);
  }

  /* back */
  .back-name {
    position: absolute;
    left: 36px; bottom: 40px;
    color: #ffffff;
    font-weight: 700;
    font-size: 26px;
    line-height: 1.05;
    letter-spacing: 1px;
  }
</style>
</head>
<body>

<section class="card card-front">
  <div class="brand">
    <div class="brand-dot"></div>
    <div class="brand-name">SUMMIT<br>COMPASS</div>
  </div>
  <div class="divider"></div>
  <div class="contact">
    <p class="contact-name">Dr. Gordon T. Feld</p>
    <p class="contact-title">President</p>
    <p class="contact-address">47 Maple Crest<br>Okotoks, AB T2Q 4M9</p>
    <p class="contact-line">
      <svg viewBox="0 0 10 10"><rect x="2.5" y="0.5" width="5" height="9" rx="1" fill="#1d7fb8"/></svg>
      (587) 555-0142
    </p>
    <p class="contact-line">
      <svg viewBox="0 0 10 10"><path d="M2 1 L4 1 L4.8 3.2 L3.6 4.2 Q4.6 6 6 6.6 L7 5.4 L9 6.2 L9 8.2 Q5 9 1.5 4.8 Q1 2.8 2 1Z" fill="#1d7fb8"/></svg>
      (403) 555-0187
    </p>
    <p class="contact-line">
      <svg viewBox="0 0 10 10"><rect x="0.5" y="2" width="9" height="6" rx="1" fill="#1d7fb8"/><path d="M0.8 2.4 L5 5.4 L9.2 2.4" stroke="#fff" stroke-width="0.8" fill="none"/></svg>
      gfeld@summitcompass.ca
    </p>
    <p class="contact-line contact-web">
      <svg viewBox="0 0 10 10"><circle cx="5" cy="5" r="4.5" fill="#1d7fb8"/><path d="M0.5 5 H9.5 M5 0.5 Q2.5 5 5 9.5 M5 0.5 Q7.5 5 5 9.5" stroke="#fff" stroke-width="0.6" fill="none"/></svg>
      www.summitcompass.ca
    </p>
  </div>
  <div class="footer-band" role="img" aria-label="Decorative layered blue wave band along the bottom of the card"></div>
</section>

<section class="card card-back">
  <div class="back-name">SUMMIT<br>COMPASS</div>
</section>

</body>
</html>
```